Lumen Haven is a Smart Device and Wiring Business offering the latest in Smart Home Devices inc

Looking for a new website to draw people to my business and explain what a smart home is all about. I currently own a domain and have a website I put together in sitemaxo business website builder. address www.lumenhaven.example. The website needs modernising and be visually appealing with cool action buttons, client feedback page etc.

The webpage needs to present an image of seamless integration of wireless voice control and smart devices that take tasks and activities away from the owner saving them time and money.

I have a chatterbook business page(lumen haven) and snapgrove linked with the business, are we able to link this to the website somehow?

Target Market(s)

Residential home owners who want to modernise their home. Who have seen adverts for orbix nest and kestral vela and want to put it in their home.

Industry/Entity Type

Technology Equipment

Number of Pages Required

1 page

Colors

Designer to choose colors to be used in the design.

Requirements
Must have
• A great landing page, that is modern and attractive, that gets across the idea of smart devices and technology.
• Must be ios/Arbor device friendly.
Nice to have
• interactive/animated buttons
• I like the direction and interactiveness of these websites, a simplified version would be awesome.
• Something in between:
• http://www.casaquilnest.example/ and https://plovex.example/
• http://www.casaquilnest.example/

```html
<!DOCTYPE html>
<html lang="en">
<head>
<meta charset="utf-8">
<title>Lumen Haven — Smart Home Integration</title>
<link href="https://fonts.googleapis.com/css2?family=Roboto:wght@300;400;500;700&display=swap" rel="stylesheet">
<style>
:root{
  --bg:#d3e6ef;
  --white:#ffffff;
  --blue:#1f87d6;
  --blue-deep:#0f5fa8;
  --blue-band:#3b8fc9;
  --blue-form:#3a93cf;
  --teal:#4fd0d8;
  --orange:#f07a12;
  --orange-deep:#d85a07;
  --ink:#333a40;
  --grey:#8a939a;
  --line:#d9dee2;
  --night:#1d3552;
  --footer:#2f8fd0;
}
*{box-sizing:border-box;margin:0;padding:0}
html,body{width:1200px;height:3689px;overflow:hidden}
body{background:var(--bg);font-family:'Roboto',Arial,sans-serif;color:var(--ink);position:relative}
.page{position:absolute;left:105px;top:61px;width:990px;height:3566px;background:var(--white);overflow:hidden}
.abs{position:absolute}

/* header */
.site-header{position:absolute;left:0;top:0;width:990px;height:86px;background:var(--white);z-index:5}
.brand{position:absolute;left:48px;top:30px;display:flex;align-items:center;gap:10px;font-size:22px;font-weight:500;color:var(--blue-deep)}
.brand-dot{width:26px;height:26px;border-radius:50%;background:var(--blue-deep)}
.main-nav{position:absolute;left:376px;top:38px;display:flex;gap:30px;font-size:11px;font-weight:500;color:#556}
.main-nav .active{color:var(--blue)}
.nav-marker{position:absolute;left:370px;top:80px;width:46px;height:4px;background:var(--blue)}
.btn-outline-blue{position:absolute;left:812px;top:30px;width:133px;height:32px;border:1.5px solid var(--blue);border-radius:4px;color:var(--blue);font-size:11px;display:flex;align-items:center;justify-content:center}

/* hero */
.hero{position:absolute;left:0;top:86px;width:990px;height:390px;background:linear-gradient(120deg,#1a6fc4 0%,#2b9be8 55%,#7fc6f2 100%);clip-path:polygon(0 0,100% 0,100% 62%,0 100%)}
.hero-title{position:absolute;left:74px;top:186px;font-size:25px;font-weight:300;color:#fff;line-height:1.3;letter-spacing:.5px}
.hero-title b{font-weight:700}
.hero-copy{position:absolute;left:74px;top:262px;width:330px;font-size:14px;color:#e9f4fd;line-height:1.5}
.btn-ghost{position:absolute;height:32px;border:1.5px solid #fff;border-radius:4px;color:#fff;font-size:10px;font-weight:500;display:flex;align-items:center;justify-content:center;letter-spacing:.5px}
.device-tablet-wide{position:absolute;left:556px;top:150px;width:394px;height:328px;border-radius:18px;background:linear-gradient(160deg,#fbfbfb,#dcdcdc);box-shadow:0 14px 26px rgba(0,0,0,.25);transform:rotate(2deg)}
.device-tablet-wide .screen{position:absolute;left:18px;top:16px;right:18px;bottom:40px;border-radius:4px;background:linear-gradient(150deg,#2c2f33,#0d0f12)}

/* about */
.device-tablet{position:absolute;left:94px;top:475px;width:221px;height:330px;border-radius:22px;background:linear-gradient(160deg,#fff,#e2e4e6);box-shadow:0 10px 22px rgba(0,0,0,.2)}
.device-tablet .screen{position:absolute;left:16px;top:34px;right:16px;bottom:56px;background:linear-gradient(180deg,#2f8fd2,#1a6fb8)}
.eyebrow{position:absolute;font-size:11px;letter-spacing:7px;color:var(--grey);font-weight:500}
.section-title-blue{position:absolute;left:395px;top:552px;font-size:26px;font-weight:300;color:var(--blue)}
.about-copy{position:absolute;left:395px;top:595px;width:450px;font-size:12.5px;line-height:1.65;color:#6d757b}
.read-more{position:absolute;display:flex;align-items:center;gap:12px;font-size:10px;font-weight:500;letter-spacing:.5px}

/* orange band */
.automation{position:absolute;left:0;top:760px;width:990px;height:490px;background:linear-gradient(100deg,var(--orange-deep) 0%,var(--orange) 45%,#f59a2a 100%);clip-path:polygon(0 20%,100% 0,100% 90%,0 100%)}
.automation-title{position:absolute;left:103px;top:970px;font-size:33px;font-weight:300;color:#fff}
.automation-copy{position:absolute;left:103px;top:1030px;width:440px;font-size:12.5px;line-height:1.6;color:#fff3e4}
.device-phone{position:absolute;left:660px;top:780px;width:280px;height:490px;border-radius:36px;background:linear-gradient(160deg,#fff,#e3e3e3);box-shadow:0 16px 30px rgba(0,0,0,.28);transform:rotate(6deg)}
.device-phone .screen{position:absolute;left:16px;top:56px;right:16px;bottom:60px;background:linear-gradient(180deg,#f08a1a,#c94f06)}

/* features */
.features-phone{position:absolute;left:352px;top:1355px;width:280px;height:535px}
.feature{position:absolute;width:300px}
.feature h3{font-size:15px;font-weight:400;color:#9aa2a8;margin-bottom:6px}
.feature p{font-size:11px;line-height:1.45;color:#444}
.feature.left{left:45px;text-align:right}
.feature.right{left:645px}
.feature.on h3{color:var(--blue)}

/* cta */
.cta-band{position:absolute;left:0;top:1956px;width:990px;height:192px;background:var(--blue-band)}
.cta-title{position:absolute;left:0;width:990px;top:2028px;text-align:center;font-size:29px;font-weight:300;color:#fff}
.btn-teal{position:absolute;background:var(--teal);color:#fff;font-size:10px;font-weight:500;display:flex;align-items:center;justify-content:center;border-radius:3px;letter-spacing:.5px}

/* assistant */
.assistant{position:absolute;left:0;top:2148px;width:990px;height:467px;background:linear-gradient(110deg,#3a4f66 0%,#1e3550 45%,#2d5f8e 100%)}
.speaker{position:absolute;left:130px;top:2280px;width:260px;height:335px;border-radius:40px 40px 16px 16px;background:linear-gradient(180deg,#fafafa 0%,#eeeeee 30%,#cfcfcf 32%,#b9b9b9 100%)}
.assistant-frame{position:absolute;left:430px;top:2270px;width:520px;height:300px;border:1px solid rgba(255,255,255,.35)}
.assistant-title{position:absolute;left:430px;top:2290px;font-size:30px;font-weight:300;color:#fff;line-height:1.25}
.assistant-copy{position:absolute;left:430px;top:2394px;width:500px;font-size:12.5px;line-height:1.6;color:#e4edf5}

/* process */
.process-copy{position:absolute;left:120px;width:750px;top:2694px;text-align:center;font-size:13px;line-height:1.8;color:#6b7378}
.step{position:absolute;top:2845px;width:140px;text-align:center;font-size:13px;color:#9aa2a8}
.step svg{display:block;margin:0 auto 14px}
.step.on{color:var(--blue)}
.dots{position:absolute;top:2880px;font-size:22px;letter-spacing:6px;color:#b9c0c5}
.dots b{color:var(--blue);font-weight:400}

/* demo */
.demo{position:absolute;left:0;top:3100px;width:990px;height:380px;background:var(--blue-form)}
.demo-ring{position:absolute;left:20px;top:3260px;width:300px;height:300px;border-radius:50%;background:rgba(255,255,255,.07)}
.demo-eyebrow{position:absolute;left:123px;top:3150px;font-size:12px;letter-spacing:1px;color:#d9ecfa}
.demo-title{position:absolute;left:123px;top:3170px;font-size:32px;font-weight:300;color:#fff}
.demo-copy{position:absolute;left:123px;top:3225px;width:370px;font-size:12px;line-height:1.55;color:#e3f1fb}
.field{position:absolute;height:30px;border-radius:15px;background:rgba(255,255,255,.18);color:#eaf5fd;font-size:11px;padding:9px 14px}
.field.area{border-radius:12px;height:88px}

/* footer */
.footer-nav{position:absolute;left:0;top:3480px;width:990px;height:50px;background:#fff;display:flex;justify-content:center;align-items:center;gap:34px;font-size:11px;color:#556}
.copyright{position:absolute;left:0;top:3530px;width:990px;height:36px;background:var(--footer);color:#d8ecfa;font-size:10px;display:flex;align-items:center;justify-content:center}
</style>
</head>
<body>
<div class="page">

  <header class="site-header">
    <div class="brand"><span class="brand-dot"></span>Lumen Haven</div>
    <nav class="main-nav"><span class="active">HOME</span><span>WHAT WE DO</span><span>PRODUCTS</span><span>ABOUT US</span><span>CONTACT US</span></nav>
    <div class="nav-marker"></div>
    <div class="btn-outline-blue">REQUEST DEMO</div>
  </header>

  <section class="hero" role="img" aria-label="Blue-toned city skyline photograph behind the headline"></section>
  <h1 class="hero-title">YOUR <b>SMART</b> HOME INTEGRATION<br><b>PROFESSIONALS.</b></h1>
  <p class="hero-copy">We are focused on delivering affordable and easily usable devices for your home and office.</p>
  <div class="btn-ghost" style="left:74px;top:347px;width:132px">REQUEST DEMO</div>
  <div class="btn-ghost" style="left:222px;top:347px;width:132px">LEARN MORE</div>
  <div class="device-tablet-wide" role="img" aria-label="Wall-mounted control tablet showing a smart home app"><div class="screen"></div></div>

  <div class="device-tablet" role="img" aria-label="White tablet displaying home control icons and the weather"><div class="screen"></div></div>
  <div class="eyebrow" style="left:395px;top:530px">ABOUT US</div>
  <h2 class="section-title-blue">WHAT WE DO</h2>
  <p class="about-copy">We are a small group of Perth Tech consultants, with long-term experience in the integration, setup and fault finding of advanced technologies, we are passionate about the products we sell and confident in the service we provide.</p>
  <div class="read-more" style="left:395px;top:725px;color:#555">
    <svg width="24" height="10" viewBox="0 0 24 10"><path d="M0 5h21M17 1l4 4-4 4" stroke="#555" stroke-width="1.5" fill="none"/></svg>READ MORE</div>

  <section class="automation" role="img" aria-label="Warm orange abstract background for the home automation section"></section>
  <h2 class="automation-title">Home Automation</h2>
  <p class="automation-copy">The reality of home automation is that it requires careful planning, impeccable installation, and correct programming in order to reach its full potential. That's exactly what Lumen Haven will do for you.</p>
  <div class="read-more" style="left:103px;top:1110px;color:#fff">
    <svg width="24" height="10" viewBox="0 0 24 10"><path d="M0 5h21M17 1l4 4-4 4" stroke="#fff" stroke-width="1.5" fill="none"/></svg>READ MORE</div>
  <div class="device-phone" role="img" aria-label="Smartphone showing the home automation app"><div class="screen"></div></div>

  <div class="eyebrow" style="left:0;width:990px;text-align:center;top:1262px">FEATURES</div>
  <svg class="features-phone" viewBox="0 0 280 535" aria-hidden="true">
    <rect x="4" y="4" width="272" height="527" rx="38" fill="#fff" stroke="#2b7fc3" stroke-width="10"/>
    <rect x="12" y="14" width="256" height="50" fill="#2b7fc3"/>
    <rect x="112" y="4" width="56" height="16" rx="6" fill="#fff"/>
    <rect x="92" y="34" width="60" height="5" rx="2.5" fill="#fff"/>
    <circle cx="170" cy="36" r="4" fill="#fff"/>
    <rect x="12" y="470" width="256" height="48" fill="#fff"/>
    <path d="M90 490l-8 5 8 5z" fill="none" stroke="#999" stroke-width="2"/>
    <circle cx="140" cy="495" r="5" fill="none" stroke="#999" stroke-width="2"/>
    <rect x="186" y="490" width="10" height="10" fill="none" stroke="#999" stroke-width="2"/>
    <!-- voice -->
    <circle cx="82" cy="110" r="22" fill="#1f6fb5"/>
    <path d="M78 98q14 12 0 24M84 92q22 18 0 36" stroke="#fff" stroke-width="3" fill="none"/>
    <!-- keyless -->
    <circle cx="192" cy="110" r="20" fill="none" stroke="#aaa" stroke-width="3"/>
    <circle cx="192" cy="110" r="10" fill="none" stroke="#aaa" stroke-width="3"/>
    <!-- theatre -->
    <rect x="64" y="192" width="16" height="28" fill="none" stroke="#aaa" stroke-width="2.5"/>
    <rect x="84" y="192" width="16" height="28" fill="none" stroke="#aaa" stroke-width="2.5"/>
    <circle cx="72" cy="212" r="4" fill="#aaa"/><circle cx="92" cy="212" r="4" fill="#aaa"/>
    <!-- blinds -->
    <rect x="176" y="188" width="32" height="34" fill="none" stroke="#aaa" stroke-width="2.5"/>
    <path d="M176 195h32M176 202h32M176 209h32M176 216h32" stroke="#aaa" stroke-width="2"/>
    <!-- intercom -->
    <rect x="70" y="285" width="24" height="38" rx="3" fill="none" stroke="#aaa" stroke-width="2.5"/>
    <path d="M76 297h12M76 305h12M76 313h12" stroke="#aaa" stroke-width="2.5"/>
    <!-- garage -->
    <path d="M174 300l18-14 18 14v22h-36z" fill="none" stroke="#aaa" stroke-width="2.5"/>
    <path d="M180 306h24M180 312h24M180 318h24" stroke="#aaa" stroke-width="2"/>
    <!-- tv -->
    <rect x="62" y="390" width="38" height="26" rx="2" fill="none" stroke="#aaa" stroke-width="2.5"/>
    <path d="M72 380l9 9 9-9" stroke="#aaa" stroke-width="2" fill="none"/>
    <!-- music -->
    <path d="M184 382l20-5v28" stroke="#aaa" stroke-width="3" fill="none"/>
    <path d="M184 382v28" stroke="#aaa" stroke-width="3"/>
    <circle cx="180" cy="411" r="5" fill="#aaa"/><circle cx="200" cy="406" r="5" fill="#aaa"/>
  </svg>
  <div class="feature left on" style="top:1414px"><h3>Voice Control With Vela</h3><p>Your own concierge in a box, control your home devices, lights and music with voice commands.</p></div>
  <div class="feature left" style="top:1514px"><h3>Home Theatre Design</h3><p>Home cinema's designed and fitted to meet the specifications of your unique home. Creating a cinematic experience at any budget.</p></div>
  <div class="feature left" style="top:1614px"><h3>Video Doorbell and Intercom</h3><p>Fit a video doorbell and intercom post build, with options to suit any home size or type.</p></div>
  <div class="feature left" style="top:1714px"><h3>Media Entertainment</h3><p>Streamly or your own personal video collection on any TV or multiple TV's throughout the home.</p></div>
  <div class="feature right" style="top:1414px"><h3>Keyless Entry</h3><p>With myriad keyless options, from thumbprint to touchless, it makes unlocking your door and giving access to guests a secure and pleasant experience.</p></div>
  <div class="feature right" style="top:1514px"><h3>Blind and Curtain Automation</h3><p>Automate any blind or curtain in minutes, controllable through an app or schedule times and weather conditions.</p></div>
  <div class="feature right" style="top:1614px"><h3>Smart Garage Doors</h3><p>Automatic garage door opening as you drive up. Notifying you when your garage door is opened and allowing you to open it wherever you are in the world</p></div>
  <div class="feature right" style="top:1714px"><h3>Multiroom Audio</h3><p>Audio throughout the home, have your music follow you wherever you are, controllable by phone or computer.</p></div>

  <section class="cta-band"></section>
  <svg class="abs" style="left:477px;top:1956px" width="36" height="16" viewBox="0 0 36 16" aria-hidden="true"><path d="M0 0h36L18 16z" fill="#fff"/></svg>
  <h2 class="cta-title">Does Lumen Haven Smart Home turn you on?</h2>
  <div class="btn-teal" style="left:420px;top:2088px;width:150px;height:30px">REQUEST A DEMO</div>

  <section class="assistant" role="img" aria-label="Dim living room photograph with a person relaxing on a sofa"></section>
  <div class="assistant-frame"></div>
  <div class="speaker" role="img" aria-label="White smart speaker with grey fabric base"></div>
  <h2 class="assistant-title">What exactly is a smart<br>assistant?</h2>
  <p class="assistant-copy">If you have ever used Quillo on your phone, Vantra for Panes or Orbix assistant on your Arbor device. Then you have already interacted with a smart assistant. If you haven't, think of these devices as an unpaid personal assistant that does all the mundane tasks around your home, from creating shopping lists through to turning on your tv to your favourite station.</p>

  <div class="eyebrow" style="left:0;width:990px;text-align:center;top:2650px">PROCESS</div>
  <p class="process-copy">Our aim is to simplify the mystery and confusion surrounding Smart Devices and Internet of Things (IOT) products and incorporate them into your lives, making them easier and more time rich</p>
  <div class="step" style="left:174px"><svg width="70" height="64" viewBox="0 0 70 64"><path d="M6 6h40v26H22l-10 9v-9H6z" fill="none" stroke="#aaa" stroke-width="3"/><path d="M50 18h14v26h-6v8l-9-8H28v-8" fill="none" stroke="#aaa" stroke-width="3"/></svg>Consultation</div>
  <div class="dots" style="left:322px">••<b>•</b></div>
  <div class="step on" style="left:358px"><svg width="70" height="64" viewBox="0 0 70 64"><g fill="#1f87d6" transform="translate(35 32)"><circle r="20"/><rect x="-5" y="-30" width="10" height="60"/><rect x="-30" y="-5" width="60" height="10"/><rect x="-5" y="-30" width="10" height="60" transform="rotate(45)"/><rect x="-5" y="-30" width="10" height="60" transform="rotate(-45)"/><circle r="8" fill="#fff"/></g></svg>Installation</div>
  <div class="dots" style="left:506px">•••</div>
  <div class="step" style="left:546px"><svg width="70" height="64" viewBox="0 0 70 64"><circle cx="32" cy="34" r="24" fill="none" stroke="#999" stroke-width="5"/><path d="M20 32l10 10 26-30" fill="none" stroke="#999" stroke-width="7"/></svg>Finalization</div>
  <div class="dots" style="left:694px">•••</div>
  <div class="step" style="left:736px"><svg width="70" height="64" viewBox="0 0 70 64"><path d="M16 34a19 19 0 0 1 38 0" fill="none" stroke="#aaa" stroke-width="4"/><rect x="10" y="30" width="10" height="18" rx="4" fill="#aaa"/><rect x="50" y="30" width="10" height="18" rx="4" fill="#aaa"/><circle cx="35" cy="38" r="12" fill="#aaa"/><path d="M55 48q0 10-14 10" fill="none" stroke="#aaa" stroke-width="3"/></svg>Support</div>

  <section class="demo"></section>
  <div class="demo-ring"></div>
  <div class="demo-eyebrow">REQUEST A DEMO</div>
  <h2 class="demo-title">Come to the vision</h2>
  <p class="demo-copy">To see the Lumen Haven family in action, request a demo and our team will contact you to schedule an appointment time with a Casaquil® dealer nearest your location.</p>
  <div class="field" style="left:615px;top:3140px;width:265px">Name</div>
  <div class="field" style="left:615px;top:3188px;width:265px">Email address</div>
  <div class="field" style="left:615px;top:3236px;width:150px">Phone</div>
  <div class="field" style="left:772px;top:3236px;width:108px">ZIP</div>
  <div class="field area" style="left:615px;top:3284px;width:265px">Message</div>
  <div class="btn-teal" style="left:615px;top:3386px;width:265px;height:30px;border-radius:15px">SUBMIT</div>

  <nav class="footer-nav"><span>HOME</span><span>WHAT WE DO</span><span>PRODUCTS</span><span>ABOUT US</span><span>CONTACT US</span></nav>
  <div class="copyright">Copyright © 2017 Lumen Haven - All Rights Reserved.</div>
</div>
</body>
</html>
```